New Business Card/Website Logo

We need a business card design for a new company based in Sydney. The company focuses mainly in construction in the field of form work and concreting. Attached is the logo being used already which can be used as a base for a new design, the current one is simply too bland and we are looking to spruce it up so it stands out and looks nicer. The logo would also be used on the website which is currently under construction. The attached image has the name, mobile and also the license number which needs to be there. The current email address on there can be removed and can be replaced with the website http://www.bravelintel.com.au, thanks!
Updates

Target Market(s)

Construction industry. Focusing on form work and concreting

Industry/Entity Type

Construction

Requirements
Must have
• License # on card along with website http://www.bravelintel.com.au and mobile phone number
Nice to have
• You have freedom with the design. The current design was a mock up done quite quickly. Please just keep in mind the target audience - construction, thanks.
Should not have
• the mailvista email address can be removed(refer picture) and replaced somewhere on the design with the website http://www.bravelintel.com.au

```html
<!DOCTYPE html>
<html lang="en">
<head>
<meta charset="utf-8">
<title>Bravelintel Construction Services – Business Card</title>
<link rel="stylesheet" href="https://fonts.googleapis.com/css2?family=Jost:wght@300;400;600&display=swap">
<style>
  :root {
    --backdrop: #5d6673;
    --card-concrete: #c9c8c4;
    --card-concrete-light: #d6d5d1;
    --engraved-ink: #5a5955;
    --engraved-highlight: rgba(255, 255, 255, 0.55);
    --engraved-shade: rgba(0, 0, 0, 0.35);
  }
  * { margin: 0; padding: 0; box-sizing: border-box; }
  html, body {
    width: 1200px;
    height: 675px;
    overflow: hidden;
    background: var(--backdrop);
    font-family: "Jost", "Futura", sans-serif;
  }
  .canvas {
    position: relative;
    width: 1200px;
    height: 675px;
  }
  .business-card {
    position: absolute;
    left: 150px;
    top: 80px;
    width: 900px;
    height: 515px;
    border-radius: 6px;
    background: radial-gradient(circle at 30% 25%, var(--card-concrete-light), var(--card-concrete) 70%);
    box-shadow: 0 10px 30px rgba(0, 0, 0, 0.35);
    color: var(--engraved-ink);
  }
  .engraved {
    text-shadow: 1px 1px 0 var(--engraved-highlight), -1px -1px 0 var(--engraved-shade);
  }
  .brand {
    position: absolute;
    left: 60px;
    top: 55px;
    display: flex;
    align-items: center;
    gap: 28px;
  }
  .brand-square {
    width: 110px;
    height: 110px;
    background: var(--engraved-ink);
    box-shadow: inset 2px 2px 3px var(--engraved-shade), 1px 1px 0 var(--engraved-highlight);
  }
  .brand-name {
    font-size: 68px;
    font-weight: 300;
    letter-spacing: 2px;
    line-height: 1;
  }
  .brand-tagline {
    font-size: 26px;
    font-weight: 400;
    margin-top: 6px;
    margin-left: 70px;
  }
  .contact {
    position: absolute;
    right: 60px;
    top: 215px;
    text-align: right;
  }
  .contact-name {
    font-size: 42px;
    font-weight: 600;
    letter-spacing: 1px;
  }
  .contact-phone {
    font-size: 30px;
    font-weight: 600;
    margin-top: 4px;
  }
  .contact-website {
    font-size: 30px;
    font-weight: 600;
    margin-top: 30px;
  }
  .licence {
    position: absolute;
    left: 60px;
    bottom: 50px;
    font-size: 34px;
    font-weight: 600;
  }
</style>
</head>
<body>
  <main class="canvas">
    <section class="business-card" aria-label="Bravelintel business card">
      <header class="brand">
        <div class="brand-square" aria-hidden="true"></div>
        <div class="brand-text">
          <div class="brand-name engraved">BRAVELINTEL</div>
          <div class="brand-tagline engraved">Construction Services</div>
        </div>
      </header>
      <div class="contact">
        <div class="contact-name engraved">Mateo Alvarez</div>
        <div class="contact-phone engraved">0412558093</div>
        <div class="contact-website engraved">http://www.bravelintel.com.au</div>
      </div>
      <div class="licence engraved">Licence: 384215B</div>
    </section>
  </main>
</body>
</html>
```